Business Card Design

We are a florist shop that also stocks a range of giftware and jewellery. I would like a new design that incorporates a light green background. If you could use a skeleton leaf somewhere in the design that would be great. I would also like to incorporate the find us on Friendlink logo on this design.

Industry/Entity Type

Florist

Contact Information for Business Card

Petals on Larkmore
41 Brindle street
Tarrin Victoria 3871
Phone: 0352983047
Fax : 0352983066
email: pol@wrenmail.net.au

Proprietors : Dana & Lee Thornwick

```html
<!DOCTYPE html>
<html lang="en">
<head>
<meta charset="utf-8">
<title>Petals on Larkmore – Business Card</title>
<link rel="stylesheet" href="https://fonts.googleapis.com/css2?family=Source+Sans+3:wght@400&display=swap">
<style>
  :root {
    --backdrop: #4a4a4c;
    --card-green: #8dc63f;
    --ink-white: #ffffff;
  }
  html, body {
    margin: 0;
    padding: 0;
    width: 1200px;
    height: 999px;
    overflow: hidden;
    background: var(--backdrop);
    font-family: "Source Sans 3", "Myriad Pro", Arial, sans-serif;
  }
  .card {
    position: absolute;
    left: 68px;
    top: 192px;
    width: 1063px;
    height: 614px;
    background: var(--card-green);
    color: var(--ink-white);
    overflow: hidden;
  }
  .brand-name {
    position: absolute;
    left: 52px;
    top: 48px;
    margin: 0;
    font-weight: 400;
    font-size: 80px;
    line-height: 1.15;
    color: var(--ink-white);
  }
  .brand-name .line-two { display: block; padding-left: 100px; }
  .floral-flourish {
    position: absolute;
    left: 648px;
    top: 0;
    width: 415px;
    height: 358px;
  }
  .proprietors {
    position: absolute;
    left: 45px;
    top: 393px;
    margin: 0;
    font-size: 34px;
    line-height: 1.1;
    font-weight: 400;
  }
  .address {
    position: absolute;
    left: 51px;
    top: 457px;
    margin: 0;
    font-style: normal;
    font-size: 27px;
    line-height: 37px;
  }
  .divider {
    position: absolute;
    left: 648px;
    top: 465px;
    width: 4px;
    height: 128px;
  }
  .contact-list {
    position: absolute;
    left: 693px;
    top: 460px;
    margin: 0;
    padding: 0;
    list-style: none;
    font-size: 28px;
    line-height: 38px;
  }
  .contact-list li { display: flex; align-items: center; }
  .contact-list svg { width: 26px; height: 24px; margin-right: 38px; fill: var(--ink-white); }
</style>
</head>
<body>
  <section class="card">
    <h1 class="brand-name">Petals<span class="line-two">on Larkmore</span></h1>

    <svg class="floral-flourish" role="img" aria-label="White swirling floral flourish with leaves" viewBox="0 0 415 358">
      <defs>
        <linearGradient id="flourish-tone" x1="0" y1="1" x2="1" y2="0">
          <stop offset="0" stop-color="#ffffff" stop-opacity="0.12"/>
          <stop offset="1" stop-color="#ffffff" stop-opacity="0.35"/>
        </linearGradient>
      </defs>
      <rect width="415" height="358" fill="url(#flourish-tone)"/>
    </svg>

    <p class="proprietors">Dana &amp; Lee Thornwick</p>

    <address class="address">
      Petals on Larkmore<br>
      41 Brindle street<br>
      Tarrin Victoria 3871
    </address>

    <svg class="divider" viewBox="0 0 4 128" aria-hidden="true">
      <path d="M2 0 L3.2 64 L2 128 L0.8 64 Z" fill="#ffffff"/>
    </svg>

    <ul class="contact-list">
      <li>
        <svg viewBox="0 0 26 24" aria-hidden="true"><path d="M6 2 L10 6 L8 9 C9 12 12 15 15 16 L18 14 L22 18 L19 22 C11 21 4 14 3 6 Z"/><path d="M14 3 A8 8 0 0 1 22 11 L20 11 A6 6 0 0 0 14 5 Z"/></svg>
        0352983047
      </li>
      <li>
        <svg viewBox="0 0 26 24" aria-hidden="true"><rect x="7" y="1" width="12" height="8"/><rect x="2" y="10" width="22" height="9" rx="1"/><rect x="5" y="20" width="16" height="3"/></svg>
        0352983066
      </li>
      <li>
        <svg viewBox="0 0 26 24" aria-hidden="true"><path d="M2 9 L13 1 L24 9 L24 22 L2 22 Z"/><path d="M6 11 L13 16 L20 11" fill="none" stroke="#8dc63f" stroke-width="2"/></svg>
        pol@wrenmail.net.au
      </li>
    </ul>
  </section>
</body>
</html>
```